Canadian company needs a packaging design for a new product line of TubGlow Hot Tub & Bath Fragran

We are looking for a packaging design for a new company based in Edmonton, Alberta Canada called TubGlow. We are developing a new product line of liquid and crystal Hot Tub & Bath Fragrances (aromatherapy) for example Lavender will be one of our fragrances. We are looking at the possibilities of using a stand up pouch and or the standard plastic bottles for our fragrance line. There will be different sizes from 150 grams to 600 grams in the crystal and 275 ml in the liquid. We would like to see bright multi-colored designs possibly with picture of the fragrance or a theme like favorite drinks or a more sensual idea. Each one of our fragrances will be a different color the main design needs to be able to have a different color of liquid or crystal in the bottle and possibly parts of the label will change colors for each fragrance. I have attached samples of another brand that we want to improve on.

Target Market(s)

Most of these fragrance are bought by women 70% men 30%
age 25 - 55

Industry/Entity Type

It Company

Requirements
Must have
• bottle size
Fragrance name
Nice to have
• Using the files below I like the circle of colors and possibly it could be made using water drops like in the file and possibly the two "S" could be designed like the third file I just added

```html
<!DOCTYPE html>
<html lang="en">
<head>
<meta charset="utf-8">
<title>TubGlow Lavender Label</title>
<link href="https://fonts.googleapis.com/css2?family=Russo+One&family=Great+Vibes&family=Roboto:wght@400;500&display=swap" rel="stylesheet">
<style>
  :root {
    --page-bg: #eceff1;
    --label-teal-top: #2aa3b0;
    --label-teal-bottom: #62c8cf;
    --navy: #35309a;
    --navy-edge: #4c57c4;
    --aqua-text: #47e0e3;
    --sky: #bfe6ff;
    --white: #ffffff;
    --coral-lilac: #c58ce8;
    --coral-yellow: #e9e03a;
    --curve-teal: #3fd6d6;
  }
  html, body {
    margin: 0;
    width: 1022px;
    height: 1200px;
    overflow: hidden;
    background: var(--page-bg);
  }
  .canvas {
    position: relative;
    width: 1022px;
    height: 1200px;
  }
  .label {
    position: absolute;
    left: 206px;
    top: 90px;
    width: 610px;
    height: 1020px;
    border-radius: 40px;
    background: linear-gradient(180deg, var(--label-teal-top), var(--label-teal-bottom));
    overflow: hidden;
  }
  .brand-mark {
    position: absolute;
    top: 50px;
    left: 0;
    right: 0;
    display: flex;
    justify-content: center;
    align-items: center;
    gap: 14px;
    font-family: "Russo One", sans-serif;
    font-size: 44px;
    color: var(--sky);
  }
  .brand-mark .dot {
    width: 22px;
    height: 22px;
    border-radius: 50%;
    background: var(--sky);
  }
  .title-box {
    position: absolute;
    left: 66px;
    top: 198px;
    width: 517px;
    height: 143px;
    box-sizing: border-box;
    background: var(--navy);
    border: 4px solid var(--navy-edge);
    outline: 3px solid var(--navy);
    outline-offset: 6px;
    display: flex;
    align-items: center;
    justify-content: center;
    font-family: "Russo One", sans-serif;
    font-size: 78px;
    color: var(--aqua-text);
    letter-spacing: 1px;
  }
  .fragrance-name {
    position: absolute;
    left: 0;
    right: 0;
    top: 318px;
    text-align: center;
    font-family: "Great Vibes", cursive;
    font-size: 140px;
    line-height: 1;
    color: var(--white);
    -webkit-text-stroke: 2px var(--navy);
    z-index: 2;
  }
  .size-corner {
    position: absolute;
    left: 187px;
    top: 616px;
    width: 423px;
    height: 404px;
  }
  .coral-art {
    position: absolute;
    left: 77px;
    top: 470px;
    width: 462px;
    height: 480px;
    border-radius: 45% 45% 20% 20%;
    background: radial-gradient(ellipse at 50% 40%, var(--coral-lilac) 0%, var(--coral-lilac) 55%, var(--coral-yellow) 100%);
    opacity: 0.9;
  }
  .volume {
    position: absolute;
    right: 40px;
    top: 880px;
    text-align: right;
    color: var(--white);
    font-family: "Roboto", sans-serif;
  }
  .volume .amount {
    font-size: 48px;
    font-weight: 500;
    line-height: 1.1;
  }
  .volume .weight {
    font-size: 24px;
    font-weight: 400;
  }
</style>
</head>
<body>
<div class="canvas">
  <div class="label">
    <div class="brand-mark"><span class="dot"></span>TubGlow</div>
    <div class="title-box">TUBGLOW</div>
    <div class="fragrance-name">Lavender</div>
    <svg class="size-corner" viewBox="0 0 423 404" aria-hidden="true">
      <path d="M423 0 L423 404 L0 404 C140 330 330 230 423 0 Z" fill="var(--navy)"/>
      <path d="M0 404 C140 330 330 230 423 0" fill="none" stroke="var(--curve-teal)" stroke-width="8"/>
    </svg>
    <div class="coral-art" role="img" aria-label="Illustration of a lilac sea fan coral with yellow branch tips"></div>
    <div class="volume">
      <div class="amount">300ml</div>
      <div class="weight">NET WT: 180</div>
    </div>
  </div>
</div>
</body>
</html>
```